Fun, challenging, and inspirational guide for life change - written by a coach, therapist and founde

I need (1) cover design for a book titled:
"THE HEART'S TOOLKIT FOR WORLD-BENDING IDEAS" - the unexpectedly useful craft of trusting yourself and stepping forward

A 2ND COVER will be need for a companion ebook, titled:
"THE HEART'S FIELD MANUAL FOR THRIVING AND JOY - 4 moves to open up and set free the boundless self by embracing your edges

These books will be used to promote a larger suite of products and services devoted to empowering and inspiring a community of OVERCOMERS.

For reference check out www.lanternmakershall.example

I've included some photos for visual reference points.

DESIGNS CONCEPTS:
CLEAN - A BLEND OF PAST AND PRESENT - MODERN AND THE SACRED) (...The Walcott Almanac meets

Target Market(s)

young and aspiring professionals and seasoned pros looking for life-changes due to feeling unfulfilled in their profession and relationships

Industry/Entity Type

Life Coaching

Font styles to use
Serif
Sans Serif

Requirements
Must have
• CREATIVITY - ORIGINALITY - WICKEDLY CLEAN DESIGN- AND IMPACTFUL TRANSLATION OF BRAND CONCEPT - COLOR AND PUNCH
Nice to have
• I included some photos as reference point - **PLEASE SEE THE PHOTOS FOR THE ROAD-ROVERS DESIGNS** - I really like the feeling they provoke - I want to give the viewer a sense of the journey that can be taken when they dive into these books.
• Basically, riff off the design profiles and colors included in the ROAD-ROVER covers.
• MUSTS INCLUDE -
• -ORIGINALITY
• - IMPACT
• - COLOR
• - ORIGINAL DESIGNS+
• +
Should not have
• STAY AWAY FROM...
• 1 OVERUSED AND TRENDY ICONS
• - ESOTERIC IMAGES
• - FLOWERY SCRIPTS
• - I AM REALLY LOOKING FOR A UPDATE OF THE TYPICAL SELF-HELP BOOK COVERS WHICH RELY TOO MUCH ON FLOWERY AND SACRED IMAGERY
• THANK YOU - feel free to unleash your creativity!

```html
<!DOCTYPE html>
<html lang="en">
<head>
<meta charset="utf-8">
<title>The Heart's Toolkit — Book Covers</title>
<link rel="stylesheet" href="https://fonts.googleapis.com/css2?family=Barlow+Condensed:wght@500&family=Barlow+Semi+Condensed:wght@600&family=Tinos:ital,wght@0,700;1,400&display=swap">
<style>
  :root {
    --stone-light: #6f757d;
    --stone-mid: #474b52;
    --stone-dark: #1c1e22;
    --arch-shadow: #121316;
    --glow-core: #fff4cc;
    --glow-warm: #efbd55;
    --glow-deep: #7a4a18;
    --street-dark: #1a120a;
    --ink: #141210;
    --tagline-gold: #f4e2a6;
    --author-pale: #e4e5e7;
  }
  html, body {
    margin: 0;
    padding: 0;
    width: 1200px;
    height: 900px;
    overflow: hidden;
    background: var(--stone-dark);
  }
  .cover-pair {
    position: relative;
    width: 1200px;
    height: 900px;
    display: flex;
  }
  .cover {
    position: relative;
    width: 600px;
    height: 900px;
    overflow: hidden;
  }
  .cover-scene {
    position: absolute;
    inset: 0;
    width: 600px;
    height: 900px;
  }
  .tagline {
    position: absolute;
    top: 42px;
    left: 0;
    width: 600px;
    margin: 0;
    text-align: center;
    font-family: "Tinos", serif;
    font-style: italic;
    font-weight: 400;
    font-size: 18px;
    line-height: 21px;
    color: var(--tagline-gold);
  }
  .title {
    position: absolute;
    left: 0;
    width: 600px;
    margin: 0;
    text-align: center;
    font-family: "Barlow Semi Condensed", sans-serif;
    font-weight: 600;
    font-size: 56px;
    line-height: 56px;
    color: var(--ink);
    text-shadow: 0 0 16px rgba(255, 244, 204, 0.7);
  }
  .title-toolkit { top: 150px; }
  .title-manual { top: 140px; }
  .subtitle {
    position: absolute;
    top: 370px;
    left: 120px;
    width: 360px;
    margin: 0;
    text-align: center;
    font-family: "Tinos", serif;
    font-weight: 700;
    font-size: 17px;
    line-height: 21px;
    color: var(--ink);
  }
  .author {
    position: absolute;
    bottom: 26px;
    left: 0;
    width: 600px;
    margin: 0;
    padding-left: 10px;
    box-sizing: border-box;
    text-align: center;
    font-family: "Barlow Condensed", sans-serif;
    font-weight: 500;
    font-size: 62px;
    line-height: 62px;
    letter-spacing: 10px;
    color: var(--author-pale);
    text-shadow: 0 2px 8px rgba(0, 0, 0, 0.7);
  }
</style>
</head>
<body>
<main class="cover-pair">

  <section class="cover cover-toolkit">
    <svg class="cover-scene" viewBox="0 0 600 900" role="img" aria-label="Photo: a lone figure in a coat walking through a stone archway into a sunlit, rain-streaked city street">
      <defs>
        <linearGradient id="stone-a" x1="0" y1="0" x2="0" y2="1">
          <stop offset="0" stop-color="var(--stone-light)"/>
          <stop offset="0.5" stop-color="var(--stone-mid)"/>
          <stop offset="1" stop-color="var(--stone-dark)"/>
        </linearGradient>
        <radialGradient id="glow-a" cx="0.5" cy="0.3" r="0.8">
          <stop offset="0" stop-color="var(--glow-core)"/>
          <stop offset="0.45" stop-color="var(--glow-warm)"/>
          <stop offset="1" stop-color="var(--glow-deep)"/>
        </radialGradient>
        <linearGradient id="street-a" x1="0" y1="0" x2="0" y2="1">
          <stop offset="0" stop-color="var(--street-dark)" stop-opacity="0"/>
          <stop offset="1" stop-color="var(--street-dark)" stop-opacity="0.9"/>
        </linearGradient>
      </defs>
      <rect width="600" height="900" fill="url(#stone-a)"/>
      <path d="M40 900 V280 C40 130 160 50 300 50 C440 50 560 130 560 280 V900 Z" fill="var(--arch-shadow)" opacity="0.75"/>
      <path d="M90 900 V290 C90 170 185 104 300 104 C415 104 511 170 511 290 V900 Z" fill="url(#glow-a)"/>
      <rect y="600" width="600" height="300" fill="url(#street-a)"/>
    </svg>
    <p class="tagline">the unexpectedly useful craft<br>of trusting yourself<br>and stepping forward</p>
    <h1 class="title title-toolkit">THE HEART'S<br>TOOLKIT FOR<br>WORLD-BENDING<br>IDEAS</h1>
    <p class="author">AUTHOR NAME</p>
  </section>

  <section class="cover cover-manual">
    <svg class="cover-scene" viewBox="0 0 600 900" role="img" aria-label="Photo: a lone figure in a coat walking through a stone archway into a sunlit, rain-streaked city street">
      <defs>
        <linearGradient id="stone-b" x1="0" y1="0" x2="0" y2="1">
          <stop offset="0" stop-color="var(--stone-light)"/>
          <stop offset="0.5" stop-color="var(--stone-mid)"/>
          <stop offset="1" stop-color="var(--stone-dark)"/>
        </linearGradient>
        <radialGradient id="glow-b" cx="0.5" cy="0.3" r="0.8">
          <stop offset="0" stop-color="var(--glow-core)"/>
          <stop offset="0.45" stop-color="var(--glow-warm)"/>
          <stop offset="1" stop-color="var(--glow-deep)"/>
        </radialGradient>
        <linearGradient id="street-b" x1="0" y1="0" x2="0" y2="1">
          <stop offset="0" stop-color="var(--street-dark)" stop-opacity="0"/>
          <stop offset="1" stop-color="var(--street-dark)" stop-opacity="0.9"/>
        </linearGradient>
      </defs>
      <rect width="600" height="900" fill="url(#stone-b)"/>
      <path d="M40 900 V280 C40 130 160 50 300 50 C440 50 560 130 560 280 V900 Z" fill="var(--arch-shadow)" opacity="0.75"/>
      <path d="M90 900 V290 C90 170 185 104 300 104 C415 104 511 170 511 290 V900 Z" fill="url(#glow-b)"/>
      <rect y="600" width="600" height="300" fill="url(#street-b)"/>
    </svg>
    <h1 class="title title-manual">THE HEART'S<br>FIELD MANUAL<br>FOR THRIVING<br>AND JOY</h1>
    <p class="subtitle">4 moves to open up and set free<br>the boundless self<br>by embracing your edges</p>
    <p class="author">AUTHOR NAME</p>
  </section>

</main>
</body>
</html>
```